Course flyer - evolutive design

We want to have a nice design for our course programm.
In fact we are school language, and our course programm change approximatively each 2 weeks§.
For that we need a design that we can modify each 2 weeks (only dates change ) by ourselves.
We used to have a classical design but we want to upgrade it with a modern and attractive design.
We can have 3 versions one for each city.
We have 3 offices: Tunis, Sousse & Sfax
Attached you can find old designs

Target Market(s)

students from 16 years old till retired people 76 years old

Industry/Entity Type

Education

Font styles to use
Sans Serif

Requirements
Must have
• clear timing for courses (date, days, timing)
• prices
• Adresse (each flyer has its own adress)
• phone Number
• Cool image
Should not have
• Racism
• Violence
• Too much stuff

```html
<!DOCTYPE html>
<html lang="fr">
<head>
<meta charset="utf-8">
<title>Lingovia – Programme des cours 2016</title>
<link rel="stylesheet" href="https://fonts.googleapis.com/css2?family=Oswald:wght@600;700&family=Russo+One&family=Ubuntu:wght@500;700&family=Lato:wght@400;700&display=swap">
<style>
  :root {
    --blue: #1b5a94;
    --blue-deep: #144270;
    --blue-bright: #1f86cf;
    --yellow: #dfe021;
    --yellow-dark: #b9ba1c;
    --ink: #3b3b3b;
    --ink-soft: #4a4a4a;
    --white: #ffffff;
  }
  * { margin: 0; padding: 0; box-sizing: border-box; }
  html, body { width: 900px; height: 1200px; overflow: hidden; background: var(--white); }
  .flyer {
    position: relative;
    width: 900px;
    height: 1200px;
    overflow: hidden;
    background: var(--white);
    font-family: "Lato", Arial, sans-serif;
    color: var(--ink);
  }
  .shapes { position: absolute; inset: 0; }

  .brand {
    position: absolute;
    left: 40px;
    top: 96px;
    display: flex;
    align-items: center;
    gap: 14px;
  }
  .brand-dot { width: 30px; height: 30px; border-radius: 50%; background: var(--yellow); }
  .brand-name {
    font-family: "Ubuntu", Arial, sans-serif;
    font-weight: 500;
    font-size: 60px;
    line-height: 1;
    color: var(--ink);
    letter-spacing: -1px;
  }

  .title { position: absolute; left: 32px; top: 296px; }
  .title-kicker,
  .title-course {
    font-family: "Oswald", Arial, sans-serif;
    font-weight: 700;
    font-size: 56px;
    line-height: 62px;
    letter-spacing: 0.5px;
  }
  .title-kicker { color: var(--yellow); }
  .title-course { color: var(--white); }
  .title-year {
    font-family: "Russo One", Arial, sans-serif;
    font-weight: 400;
    font-size: 80px;
    line-height: 1;
    color: var(--white);
    margin-left: -12px;
    margin-top: 2px;
    letter-spacing: 4px;
    transform: scaleX(1.42);
    transform-origin: left center;
  }

  .pill {
    position: absolute;
    left: 56px;
    width: 450px;
    height: 36px;
    border-radius: 18px;
    background: linear-gradient(90deg, var(--yellow), var(--yellow-dark));
    font-family: "Ubuntu", Arial, sans-serif;
    font-weight: 700;
    font-size: 25px;
    line-height: 36px;
    color: var(--blue);
    padding-left: 34px;
  }
  .dates {
    position: absolute;
    font-weight: 700;
    font-size: 19px;
    color: var(--ink-soft);
    white-space: nowrap;
  }
  .codes {
    position: absolute;
    list-style: none;
    font-size: 16.5px;
    line-height: 20.5px;
    color: var(--ink-soft);
    white-space: nowrap;
  }

  .notice {
    position: absolute;
    left: 588px;
    top: 578px;
    width: 276px;
    font-size: 17px;
    line-height: 21.5px;
    color: var(--white);
    text-align: justify;
  }

  .contact {
    position: absolute;
    top: 1145px;
    font-family: "Ubuntu", Arial, sans-serif;
    font-weight: 700;
    font-size: 25px;
    line-height: 36px;
    white-space: nowrap;
  }
  .contact-phone { left: 47px; color: var(--ink); }
  .contact-mail { left: 300px; color: var(--blue); }
  .contact-web { left: 620px; color: var(--yellow); font-size: 29px; }
</style>
</head>
<body>
<main class="flyer">
  <svg class="shapes" width="900" height="1200" viewBox="0 0 900 1200">
    <defs>
      <linearGradient id="bandGrad" x1="0" y1="0" x2="0" y2="1">
        <stop offset="0" stop-color="#1f6aa6"/>
        <stop offset="1" stop-color="#144270"/>
      </linearGradient>
      <linearGradient id="panelGrad" x1="0" y1="0" x2="0" y2="1">
        <stop offset="0" stop-color="#cbce22"/>
        <stop offset="1" stop-color="#9d9e26"/>
      </linearGradient>
      <linearGradient id="photoGrad" x1="0" y1="0" x2="1" y2="1">
        <stop offset="0" stop-color="#c9a77c"/>
        <stop offset="0.5" stop-color="#3f8f9c"/>
        <stop offset="1" stop-color="#8a2a4a"/>
      </linearGradient>
      <linearGradient id="studentGrad" x1="0" y1="0" x2="0" y2="1">
        <stop offset="0" stop-color="#d6587e"/>
        <stop offset="0.45" stop-color="#c64b73"/>
        <stop offset="0.55" stop-color="#8fb0d6"/>
        <stop offset="1" stop-color="#6f93c4"/>
      </linearGradient>
    </defs>

    <rect class="rule" x="0" y="259" width="445" height="4" fill="var(--blue)"/>

    <rect class="info-panel" x="548" y="470" width="352" height="650" fill="url(#panelGrad)"/>
    <rect class="panel-stripe" x="548" y="500" width="352" height="8" fill="var(--blue-bright)"/>

    <circle class="photo-ring" cx="712" cy="205" r="282" fill="none" stroke="var(--yellow)" stroke-width="16"/>

    <rect class="title-band" x="0" y="276" width="560" height="234" fill="url(#bandGrad)"/>

    <g role="img" aria-label="Photo : étudiants souriants travaillant ensemble autour d'un livre">
      <circle cx="712" cy="205" r="268" fill="url(#photoGrad)" stroke="var(--blue)" stroke-width="3"/>
    </g>

    <g role="img" aria-label="Photo : étudiante debout avec sac à dos et téléphone">
      <rect x="655" y="752" width="128" height="362" rx="20" fill="url(#studentGrad)" opacity="0.9"/>
    </g>

    <rect class="footer-rule" x="0" y="1116" width="900" height="8" fill="var(--blue)"/>
    <polygon class="footer-blue" points="548,1124 900,1124 900,1200 595,1200" fill="var(--blue)"/>
    <polygon class="footer-yellow" points="0,1124 548,1124 595,1200 0,1200" fill="var(--yellow)"/>
  </svg>

  <header class="brand">
    <span class="brand-name">lingovia</span>
    <span class="brand-dot"></span>
  </header>

  <h1 class="title">
    <div class="title-kicker">COORS</div>
    <div class="title-course">ITALLEMAND IC</div>
    <div class="title-year">2016</div>
  </h1>

  <section class="schedule schedule-intensive">
    <h2 class="pill" style="top:564px">Intensif (Lundi-vendreo)</h2>
    <p class="dates" style="left:40px; top:602px">07/03/2016 - 25/03/2016</p>
    <p class="dates" style="left:301px; top:602px">28/03/2016 - 15/04/2016</p>
    <ul class="codes" style="left:91px; top:632px">
      <li>A1.1 DKS2090</li><li>B1.1 DKS2098</li><li>A1.2 OKS2091</li><li>B1.2 DKS2099</li>
      <li>A2.1 ogs202</li><li>B2.1 DKS2094</li><li>A2.2 DKS2093</li>
    </ul>
    <ul class="codes" style="left:358px; top:635px">
      <li>A1.1 DKS2105</li><li>B1.1 DKS2113</li><li>B1.2 DKS2114</li><li>B2.1 DKS2107</li>
      <li>B1 OKS2109</li><li>A2.2 OKS2108</li>
    </ul>
  </section>

  <section class="schedule schedule-semi">
    <h2 class="pill" style="top:808px">EXterlSit (3jour/semaine)</h2>
    <p class="dates" style="left:40px; top:856px">28/03/2016 - 22/04/2016</p>
    <ul class="codes" style="left:91px; top:890px">
      <li>A1.1 OKS2121</li><li>A1.2 DKS2122</li>
    </ul>
    <ul class="codes" style="left:356px; top:890px">
      <li>A2.2 DKS2124</li>
    </ul>
  </section>

  <section class="schedule schedule-extensive">
    <h2 class="pill" style="top:974px">Extensif (2jour/sernaine)</h2>
    <p class="dates" style="left:44px; top:1015px">28/03/2016 &nbsp;- 05/05/2016</p>
    <ul class="codes" style="left:94px; top:1044px">
      <li>A1.1 DKS2115</li><li style="margin-left:-6px">A2.2 OKS2118</li>
    </ul>
    <ul class="codes" style="left:344px; top:1044px">
      <li>A1.2 DKS2116</li><li>B1.1 DKS2119</li>
    </ul>
  </section>

  <p class="notice">Toute inscription dolt im-pera-tivement se faire au plus tard une semaine avant le debut des cours. Nombre minimum de 5 partici-pants requis L'horaire des cours est susceptible d'être modifie. Prix par module &nbsp;340 TND.</p>

  <footer>
    <span class="contact contact-phone">+216 71 400 00</span>
    <span class="contact contact-mail">tunis@lingovia.org</span>
    <span class="contact contact-web">www.lingovia.org</span>
  </footer>
</main>
</body>
</html>
```